Letterhead creation for military law attorney

I need letterhead design for my business. We are now only doing military law and need to change address, logo and vision. I like the idea of using an eagle or a jolly roger flag

Target Market(s)

Military Law Clients

Colors
3176b5
85abd2

Requirements
Must have
• We are defending people against the government
Nice to have
• Jolly Roger Flag

```html
<!DOCTYPE html>
<html lang="en">
<head>
<meta charset="UTF-8">
<title>Harlan Vance Defense – Letterhead</title>
<link href="https://fonts.googleapis.com/css2?family=Poppins:wght@400;500;600;700&display=swap" rel="stylesheet">
<style>
  :root {
    --brand-dark: #3176b5;
    --brand-light: #85abd2;
    --paper: #ffffff;
    --ink: #1f1f24;
    --backdrop: #0c1a22;
  }
  * { box-sizing: border-box; margin: 0; padding: 0; }
  html, body {
    width: 1200px; height: 1070px; overflow: hidden;
    background: var(--backdrop);
    font-family: "Poppins", sans-serif;
  }
  .letterhead {
    position: absolute; left: 243px; top: 30px;
    width: 714px; height: 1010px;
    background: var(--paper);
    overflow: hidden;
  }
  .band { position: absolute; left: 0; width: 100%; display: flex; }
  .band span { display: block; height: 100%; }
  .band-top { top: 0; height: 39px; }
  .band-top .light { width: 72%; background: var(--brand-light); }
  .band-top .dark { flex: 1; background: var(--brand-dark); }
  .rule-top { position: absolute; top: 45px; left: 0; width: 100%; height: 10px; background: var(--brand-dark); }
  .rule-bottom { position: absolute; bottom: 46px; left: 0; width: 100%; height: 10px; background: var(--brand-dark); }
  .band-bottom { bottom: 0; height: 40px; }
  .band-bottom .light { width: 24%; background: var(--brand-light); }
  .band-bottom .dark { flex: 1; background: var(--brand-dark); }

  .brand {
    position: absolute; left: 66px; top: 150px;
    display: flex; align-items: center; gap: 10px;
    color: var(--brand-dark); font-weight: 600; font-size: 17px;
  }
  .brand-dot { width: 14px; height: 14px; border-radius: 50%; background: var(--brand-dark); }

  .contact { position: absolute; left: 512px; top: 140px; list-style: none; }
  .contact li {
    display: flex; align-items: flex-start; gap: 7px;
    font-size: 9.5px; color: var(--ink); line-height: 12px;
    margin-bottom: 20px;
  }
  .contact li:last-child { margin-bottom: 0; margin-top: -6px; }
  .contact svg { width: 18px; height: 18px; flex: none; }

  .divider {
    position: absolute; left: 75px; top: 268px; width: 570px; height: 2px;
    background: var(--brand-light);
  }
  .divider::after {
    content: ""; position: absolute; left: 40%; width: 20%; top: -0.5px; height: 3px;
    background: var(--brand-dark);
  }

  .recipient { position: absolute; left: 78px; top: 338px; color: var(--ink); }
  .recipient .label { font-size: 17px; font-weight: 400; line-height: 21px; }
  .recipient .name, .recipient .line { font-size: 16px; font-weight: 600; line-height: 21px; }
  .date { position: absolute; right: 82px; top: 344px; font-size: 16px; font-weight: 600; color: var(--ink); }

  .body {
    position: absolute; left: 80px; top: 424px; width: 578px;
    font-size: 14.2px; line-height: 20.6px; color: var(--ink);
    text-align: justify;
  }
  .body p { margin-bottom: 21px; }
</style>
</head>
<body>
  <main class="letterhead">
    <div class="band band-top"><span class="light"></span><span class="dark"></span></div>
    <div class="rule-top"></div>

    <div class="brand"><span class="brand-dot"></span>Harlan Vance Defense</div>

    <ul class="contact">
      <li>
        <svg viewBox="0 0 18 18"><rect width="18" height="18" fill="#3176b5"/><rect x="6" y="3.5" width="6" height="11" rx="1" fill="none" stroke="#fff" stroke-width="1.2"/><circle cx="9" cy="12.5" r="0.7" fill="#fff"/></svg>
        (555)013-2040
      </li>
      <li>
        <svg viewBox="0 0 18 18"><rect width="18" height="18" fill="#3176b5"/><rect x="3.5" y="8" width="11" height="6" rx="1" fill="none" stroke="#fff" stroke-width="1.2"/><path d="M6 8V5h6v3" fill="none" stroke="#fff" stroke-width="1.2"/></svg>
        (555)013-2041
      </li>
      <li>
        <svg viewBox="0 0 18 18"><rect width="18" height="18" fill="#3176b5"/><path d="M9 3.5a3.5 3.5 0 0 1 3.5 3.5c0 2.6-3.5 6-3.5 6S5.5 9.6 5.5 7A3.5 3.5 0 0 1 9 3.5z" fill="#fff"/><circle cx="9" cy="7" r="1.2" fill="#3176b5"/><path d="M4 14.5h10" stroke="#fff" stroke-width="1.2"/></svg>
        <span>PO Box 812 Fort Ridge,<br>TN 37999</span>
      </li>
    </ul>

    <div class="divider"></div>

    <div class="recipient">
      <div class="label">To</div>
      <div class="name">LOREM IPSUM</div>
      <div class="line">simply dummy text</div>
    </div>
    <div class="date">DATE: 15.08.2019</div>

    <section class="body">
      <p>Lorem Ipsum is simply dummy text of the printing and typesetting industry. Lorem Ipsum has been the industry's standard dummy text ever since the 1500s, when an unknown printer took a galley of type and scrambled it to make a type specimen book. It has survived not only five centuries, but also the leap into electronic typesetting, remaining essentially unchanged. It was popularised in the 1960s with the release of Typeline sheets containing Lorem Ipsum passages, and more recently with desktop publishing software like Quillset Layout including versions of Lorem Ipsum.</p>
      <p>Lorem Ipsum is simply dummy text of the printing and typesetting industry. Lorem Ipsum has been the industry's standard dummy text ever since the 1500s, when an unknown printer took a galley of type and scrambled it to make a type specimen book. It has survived not only five centuries, but also the leap into electronic typesetting, remaining essentially unchanged.</p>
      <p>It was popularised in the 1960s with the release of Typeline sheets containing Lorem Ipsum passages, and more recently with desktop publishing software like Quillset Layout including versions of Lorem Ipsum.</p>
    </section>

    <div class="rule-bottom"></div>
    <div class="band band-bottom"><span class="light"></span><span class="dark"></span></div>
  </main>
</body>
</html>
```